Would like to reproduce this screen to look more modern

My app is a place for farmers to post jobs a when needing help around the Farm, and local farmhands can apply for the job. The Farmer can then review multiple applicants and select the one best fit for the task at hand. I'm trying to give my screens an updated look while keeping my current color scheme and flow. I would like for you guys to recreate this screen with an updated look the best you can. The main screen with the PX will stay the same. I put that in there to show our logo and our main colors. They look outdated. the other 2 screens are looking at the customers profile, and the screen that u fill out to post a new job.

Target Market(s)

Farmers and farm employees inside the US

Industry/Entity Type

Agriculture

Requirements
Must have
• the same components for the flow but a new look
Nice to have
• ...
Should not have
• Should not change any features, but we can change how buttons look

```html
<!DOCTYPE html>
<html lang="en">
<head>
<meta charset="utf-8">
<title>PX – Profile and Create Job screens</title>
<link rel="stylesheet" href="https://fonts.googleapis.com/css2?family=Raleway:wght@300;400;500;600&display=swap">
<style>
  :root {
    --bg: #999999;
    --green-light: #34ae4c;
    --green-dark: #07913f;
    --green-text: #139a45;
    --ink: #2c2c2c;
    --muted: #a3a3a3;
    --rule: #cfcfcf;
    --navy: #1e1d5c;
    --star: #f2a744;
    --skin: #f6cd9c;
    --screen: #ffffff;
  }
  * { box-sizing: border-box; margin: 0; padding: 0; }
  html, body { width: 1200px; height: 1088px; overflow: hidden; }
  body {
    background: var(--bg);
    font-family: "Raleway", sans-serif;
    color: var(--ink);
    position: relative;
  }
  .screen {
    position: absolute;
    top: 95px;
    width: 414px;
    height: 897px;
    border-radius: 42px;
    background: var(--screen);
    overflow: hidden;
  }
  .screen--profile { left: 131px; }
  .screen--job { left: 655px; }

  .header-wave { position: absolute; left: 0; top: 0; width: 414px; }
  .scene-fill {
    position: absolute; left: 0; right: 0; bottom: 0; height: 300px;
    background: linear-gradient(180deg, rgba(240,240,240,0) 0%, rgba(236,236,236,.7) 100%);
  }
  .abs { position: absolute; transform: translateY(-50%); white-space: nowrap; }
  .center { left: 0; right: 0; text-align: center; }

  .status-time { right: 40px; top: 24px; color: #fff; font-size: 14px; font-weight: 500; }
  .status-icons { left: 32px; top: 24px; }

  .brand { top: 88px; color: #fff; font-size: 36px; font-weight: 600; letter-spacing: 2px; }
  .title { top: 146px; color: #fff; font-size: 29px; font-weight: 300; letter-spacing: .5px; }
  .title b { font-weight: 500; }
  .title-arrow { position: absolute; left: 50%; top: 167px; transform: translateX(-50%); }

  /* profile */
  .avatar {
    position: absolute; left: 134px; top: 196px; width: 146px; height: 146px;
    border-radius: 50%; background: radial-gradient(circle at 50% 40%, #f8d6ab, var(--skin));
    border: 4px solid #fff;
  }
  .rating-star { position: absolute; left: 350px; top: 298px; }
  .rating-count { left: 350px; width: 45px; text-align: center; top: 354px; color: var(--star); font-size: 18px; }
  .user-name { top: 366px; color: var(--green-text); font-size: 25px; font-weight: 400; }
  .user-phone { top: 393px; font-size: 14px; }

  .detail-row {
    position: absolute; left: 30px; width: 354px; height: 40px;
    border-bottom: 1px solid var(--rule);
    display: flex; align-items: center;
  }
  .detail-row .label { font-size: 15.5px; margin-left: 8px; flex: 1; }
  .detail-row .action { font-size: 12.5px; color: var(--muted); display: flex; align-items: center; gap: 4px; }
  .icon { width: 28px; height: 22px; flex: none; }

  .badge {
    width: 22px; height: 22px; border-radius: 50%; background: var(--navy);
    color: #fff; font-size: 11px; font-weight: 600;
    display: inline-flex; align-items: center; justify-content: center; margin-right: 8px;
  }

  .jobs-panel {
    position: absolute; left: 30px; top: 638px; width: 354px; height: 300px;
    border-left: 1px solid var(--rule); border-right: 1px solid var(--rule);
  }
  .jobs-panel__head {
    height: 29px; border-radius: 8px 8px 0 0;
    background: linear-gradient(90deg, var(--green-dark), var(--green-light));
    color: #fff; font-size: 14.5px; text-align: center; line-height: 29px; position: relative;
  }
  .jobs-panel__head::after {
    content: ""; position: absolute; left: 50%; bottom: -6px; margin-left: -6px;
    border-left: 6px solid transparent; border-right: 6px solid transparent;
    border-top: 6px solid #1ba049;
  }
  .job-row {
    position: absolute; left: 0; width: 352px; height: 46px;
    border-bottom: 1px solid var(--rule); display: flex; align-items: center; padding: 0 12px;
  }
  .job-row .label { font-size: 15.5px; margin-left: 8px; flex: 1; }
  .job-row .action { font-size: 12.5px; color: #c4c4c4; display: flex; align-items: center; gap: 8px; }

  /* create job */
  .field {
    position: absolute; left: 30px; width: 354px; height: 38px;
    border-bottom: 1px solid var(--rule); display: flex; align-items: center;
  }
  .field .label { font-size: 15.5px; margin-left: 8px; flex: 1; }
  .sorter { width: 12px; height: 22px; flex: none; }
  .rate-option {
    position: absolute; top: 381px; width: 100px; height: 100px; border-radius: 50%;
    border: 1px solid #c7c7c7; text-align: center; font-size: 15px; line-height: 18px;
    padding-top: 20px;
  }
  .radio {
    display: block; width: 14px; height: 14px; margin: 0 auto 6px;
    border: 1px solid #333; border-radius: 50%; position: relative;
  }
  .radio--on::after {
    content: ""; position: absolute; inset: 2px; border-radius: 50%; background: #222;
  }
  .range { position: absolute; top: 488px; height: 34px; border-bottom: 1px solid var(--rule); font-size: 15.5px; line-height: 30px; }
  .create-button {
    position: absolute; left: 76px; top: 813px; width: 262px; height: 48px;
    border-radius: 24px; border: none;
    background: linear-gradient(90deg, var(--green-light), var(--green-dark));
    color: #fff; font-family: "Raleway", sans-serif; font-size: 20px; letter-spacing: 3px;
    display: flex; align-items: center; justify-content: center; gap: 8px;
  }
</style>
</head>
<body>

<!-- PROFILE SCREEN -->
<section class="screen screen--profile" aria-label="My profile">
  <div class="scene-fill" role="img" aria-label="Faint sketch of a farm scene with barn and windmill"></div>
  <svg class="header-wave" width="414" height="270" viewBox="0 0 414 270" aria-hidden="true">
    <defs><linearGradient id="gp" x1="0" x2="1"><stop offset="0" stop-color="#34ae4c"/><stop offset="1" stop-color="#07913f"/></linearGradient></defs>
    <path d="M0 0H414V226Q207 320 0 226Z" fill="#07913f"/>
    <path d="M0 0H414V220Q207 300 0 220Z" fill="url(#gp)"/>
  </svg>
  <svg class="abs status-icons" width="56" height="12" viewBox="0 0 56 12" aria-hidden="true">
    <rect x="0" y="8" width="2" height="3" fill="#fff"/><rect x="4" y="6" width="2" height="5" fill="#fff"/>
    <rect x="8" y="3" width="2" height="8" fill="#fff"/><rect x="12" y="0" width="2" height="11" fill="#fff"/>
    <rect x="28" y="1" width="24" height="10" rx="4" fill="none" stroke="#fff" stroke-width="1.4"/><rect x="31" y="3.5" width="18" height="5" rx="2" fill="#fff"/>
  </svg>
  <div class="abs status-time">12:29</div>
  <div class="abs center brand">PX</div>
  <div class="abs center title"><b>MY</b> PROFILE</div>
  <svg class="title-arrow" width="62" height="10" viewBox="0 0 62 10" aria-hidden="true"><path d="M0 5H60M55 2L60 5L55 8" stroke="#fff" stroke-width="1.4" fill="none"/></svg>

  <div class="avatar" role="img" aria-label="Illustrated avatar of a farmer in a straw hat"></div>
  <svg class="rating-star" width="45" height="44" viewBox="0 0 24 23" aria-hidden="true"><path d="M12 0l3.5 7.6 8.3.9-6.2 5.6 1.8 8.2L12 18.1 4.6 22.3l1.8-8.2L.2 8.5l8.3-.9z" fill="#f2a744"/></svg>
  <div class="abs rating-count">0</div>
  <div class="abs center user-name">Daniel Hartwell</div>
  <div class="abs center user-phone">5550142087</div>

  <div class="detail-row" style="top:416px">
    <svg class="icon" viewBox="0 0 28 22" fill="none" stroke="#888" stroke-width="1"><rect x="1" y="1" width="26" height="20" rx="2"/><circle cx="9" cy="9" r="3"/><path d="M4 17c1-4 9-4 10 0M17 8h7M17 12h7"/></svg>
    <span class="label">User Details</span><span class="action">Edit Details <svg width="11" height="11" viewBox="0 0 11 11" fill="none" stroke="#aaa"><path d="M1 2h5M1 2v8h8V6M4 7l1-3 5-4 1 1-5 5z"/></svg></span>
  </div>
  <div class="detail-row" style="top:465px">
    <svg class="icon" viewBox="0 0 28 22" fill="none" stroke="#888" stroke-width="1"><path d="M1 8l13-6 13 6-13 6zM6 11v6c4 3 12 3 16 0v-6M2 9v8"/></svg>
    <span class="label">Education Detaails</span><span class="action">Edit Details <svg width="11" height="11" viewBox="0 0 11 11" fill="none" stroke="#aaa"><path d="M1 2h5M1 2v8h8V6M4 7l1-3 5-4 1 1-5 5z"/></svg></span>
  </div>
  <div class="detail-row" style="top:515px">
    <svg class="icon" viewBox="0 0 28 22" fill="none" stroke="#888" stroke-width="1"><circle cx="10" cy="6" r="3"/><path d="M4 21v-7c0-3 12-3 12 0v7M21 2v19M19 2v4h4V2"/></svg>
    <span class="label">Farm Details</span><span class="action">Edit Details <svg width="11" height="11" viewBox="0 0 11 11" fill="none" stroke="#aaa"><path d="M1 2h5M1 2v8h8V6M4 7l1-3 5-4 1 1-5 5z"/></svg></span>
  </div>
  <div class="detail-row" style="top:565px">
    <svg class="icon" viewBox="0 0 28 22" fill="none" stroke="#888" stroke-width="1"><path d="M1 21l6-10h14l6 10zM7 21l4-10M14 21v-10M21 21l-4-10"/><circle cx="20" cy="5" r="3"/></svg>
    <span class="label">Farm Images</span><span class="badge">1</span><span class="action">Edit Details <svg width="11" height="11" viewBox="0 0 11 11" fill="none" stroke="#aaa"><path d="M1 2h5M1 2v8h8V6M4 7l1-3 5-4 1 1-5 5z"/></svg></span>
  </div>

  <div class="jobs-panel">
    <div class="jobs-panel__head">PX JOBS</div>
    <div class="job-row" style="top:35px">
      <svg class="icon" viewBox="0 0 28 22" fill="none" stroke="#999"><rect x="2" y="1" width="22" height="18" rx="2"/><path d="M6 8h14M6 12h10"/></svg>
      <span class="label">Applied Jobs</span><span class="badge">1</span>
      <span class="action">View Details <svg width="16" height="12" viewBox="0 0 16 12" fill="none" stroke="#aaa"><path d="M1 1h3v3H1zM1 8h3v3H1zM6 2h9M6 5h9M6 9h9"/></svg></span>
    </div>
    <div class="job-row" style="top:81px">
      <svg class="icon" viewBox="0 0 28 22" fill="none" stroke="#999"><rect x="8" y="1" width="18" height="16" rx="1"/><path d="M12 6h10M12 10h10"/><circle cx="7" cy="16" r="5"/></svg>
      <span class="label">Scheduled Jobs</span><span class="badge">0</span>
      <span class="action">View Details <svg width="16" height="12" viewBox="0 0 16 12" fill="none" stroke="#aaa"><path d="M1 1h3v3H1zM1 8h3v3H1zM6 2h9M6 5h9M6 9h9"/></svg></span>
    </div>
    <div class="job-row" style="top:128px">
      <svg class="icon" viewBox="0 0 28 22" fill="none" stroke="#999"><circle cx="10" cy="6" r="4"/><path d="M3 21v-5c0-4 14-4 14 0v5"/><rect x="17" y="11" width="9" height="9"/></svg>
      <span class="label">Received Jobs</span><span class="badge">2</span>
      <span class="action">View Details <svg width="16" height="12" viewBox="0 0 16 12" fill="none" stroke="#aaa"><path d="M1 1h3v3H1zM1 8h3v3H1zM6 2h9M6 5h9M6 9h9"/></svg></span>
    </div>
    <div class="job-row" style="top:174px">
      <svg class="icon" viewBox="0 0 28 22" fill="none" stroke="#999"><path d="M14 1l3.5 7 7.5 1-5.5 5 1.5 7.5L14 18l-7 3.5 1.5-7.5L3 9l7.5-1z"/></svg>
      <span class="label">Favorite Jobs</span><span class="badge">0</span>
      <span class="action">View Details <svg width="16" height="12" viewBox="0 0 16 12" fill="none" stroke="#aaa"><path d="M1 1h3v3H1zM1 8h3v3H1zM6 2h9M6 5h9M6 9h9"/></svg></span>
    </div>
    <div class="job-row" style="top:220px">
      <svg class="icon" viewBox="0 0 28 22" fill="none" stroke="#999"><rect x="7" y="2" width="14" height="19" rx="1"/><path d="M11 1h6v3h-6zM10 9h8M10 13h8M10 17h5"/></svg>
      <span class="label">Completed Jobs</span><span class="badge">2</span>
      <span class="action">View Details <svg width="16" height="12" viewBox="0 0 16 12" fill="none" stroke="#aaa"><path d="M1 1h3v3H1zM1 8h3v3H1zM6 2h9M6 5h9M6 9h9"/></svg></span>
    </div>
  </div>
</section>

<!-- CREATE JOB SCREEN -->
<section class="screen screen--job" aria-label="Create new job">
  <div class="scene-fill" style="height:420px" role="img" aria-label="Faint sketch of a farm scene with barn, windmill and fence"></div>
  <svg class="header-wave" width="414" height="220" viewBox="0 0 414 220" aria-hidden="true">
    <defs><linearGradient id="gj" x1="0" x2="1"><stop offset="0" stop-color="#34ae4c"/><stop offset="1" stop-color="#07913f"/></linearGradient></defs>
    <path d="M0 0H414V164Q207 250 0 164Z" fill="#34ae4c"/>
    <path d="M0 0H414V158Q207 240 0 158Z" fill="url(#gj)"/>
  </svg>
  <svg class="abs status-icons" width="56" height="12" viewBox="0 0 56 12" aria-hidden="true">
    <rect x="0" y="8" width="2" height="3" fill="#fff"/><rect x="4" y="6" width="2" height="5" fill="#fff"/>
    <rect x="8" y="3" width="2" height="8" fill="#fff"/><rect x="12" y="0" width="2" height="11" fill="#fff"/>
    <rect x="28" y="1" width="24" height="10" rx="4" fill="none" stroke="#fff" stroke-width="1.4"/><rect x="31" y="3.5" width="18" height="5" rx="2" fill="#fff"/>
  </svg>
  <div class="abs status-time">12:29</div>
  <div class="abs center brand">PX</div>
  <div class="abs center title"><b>CREATE</b> NEW JOB</div>
  <svg class="title-arrow" width="62" height="10" viewBox="0 0 62 10" aria-hidden="true"><path d="M0 5H60M55 2L60 5L55 8" stroke="#fff" stroke-width="1.4" fill="none"/></svg>

  <div class="field" style="top:246px">
    <svg class="icon" viewBox="0 0 28 22" fill="none" stroke="#999"><path d="M1 1h5v5H1zM1 9h5v5H1zM1 17h5v4H1zM9 1h18v5H9zM9 9h18v5H9zM9 17h18v4H9z"/></svg>
    <span class="label">Select Job Category</span>
    <svg class="sorter" viewBox="0 0 12 22"><path d="M6 0l6 9H0zM6 22l6-9H0z" fill="#222"/></svg>
  </div>
  <div class="field" style="top:310px">
    <svg class="icon" viewBox="0 0 28 22" fill="none" stroke="#999"><rect x="1" y="1" width="26" height="20"/><path d="M1 5h26M4 10h10M4 14h10M4 18h10"/><rect x="17" y="10" width="7" height="8"/></svg>
    <span class="label">Job Title</span>
  </div>

  <div class="rate-option" style="left:30px"><span class="radio radio--on"></span>Hourly<br>Rate ($)</div>
  <div class="rate-option" style="left:157px"><span class="radio"></span>Fixed<br>Salary ($)</div>
  <div class="rate-option" style="left:284px"><span class="radio"></span>Per<br>Acre ($)</div>

  <div class="range" style="left:30px;width:164px">From</div>
  <div class="range" style="left:220px;width:164px">To</div>

  <div class="field" style="top:547px">
    <svg class="icon" viewBox="0 0 28 22" fill="none" stroke="#999"><rect x="1" y="1" width="24" height="20" rx="2"/><path d="M5 7h8M9 7v10M15 10h6M15 14h6"/></svg>
    <span class="label">Select Job Type</span>
    <svg class="sorter" viewBox="0 0 12 22"><path d="M6 0l6 9H0zM6 22l6-9H0z" fill="#222"/></svg>
  </div>
  <div class="field" style="top:613px">
    <svg class="icon" viewBox="0 0 28 22" fill="none" stroke="#999"><path d="M2 20l10-10M8 6l8 8M14 4l4-3 3 3-3 4M20 10l6 6-3 3-6-6"/></svg>
    <span class="label">Select Equipments Provided</span>
    <svg class="sorter" viewBox="0 0 12 22"><path d="M6 0l6 9H0zM6 22l6-9H0z" fill="#222"/></svg>
  </div>
  <div class="field" style="top:677px">
    <svg class="icon" viewBox="0 0 28 22" fill="none" stroke="#999"><path d="M7 1h12M7 21h12M9 1c0 7 8 7 8 10s-8 3-8 10M17 1c0 7-8 7-8 10s8 3 8 10"/></svg>
    <span class="label">Select Start Date and Time</span>
    <svg class="sorter" viewBox="0 0 12 22"><path d="M6 0l6 9H0zM6 22l6-9H0z" fill="#222"/></svg>
  </div>
  <div class="field" style="top:741px">
    <svg class="icon" viewBox="0 0 28 22" fill="none" stroke="#999"><path d="M7 1h12M7 21h12M9 1c0 7 8 7 8 10s-8 3-8 10M17 1c0 7-8 7-8 10s8 3 8 10"/></svg>
    <span class="label">Select End Date and Time</span>
    <svg class="sorter" viewBox="0 0 12 22"><path d="M6 0l6 9H0zM6 22l6-9H0z" fill="#222"/></svg>
  </div>

  <button class="create-button" type="button">CREATE JOB
    <svg width="46" height="10" viewBox="0 0 46 10" aria-hidden="true"><path d="M0 5H44M39 2L44 5L39 8" stroke="#fff" stroke-width="1.6" fill="none"/></svg>
  </button>
</section>

</body>
</html>
```